Landscaping flier 2024

Create a 1 page flier for landscaping services
1. Must be completed in Adobe Photoshop
2. Size 8.5" x 11" (portrait layout)
3. Include logo
4. Text to include:
2024 Gravesite Landscaping Packages
info@elmbrookmemorial.org
(201) 555-0143
elmbrookmemorial.org
5. Use chart text for the content. DO NOT COPY THE CHART DESIGN/FORMAT. Use the chart for the text you need only.
6. Use "Pricing cards as format for laying out the chart". Open to other ideas as well.
**Use the example of chart design (handwritten) to base your design off of.
7. Photos
-include before and after care photos

```html
<!DOCTYPE html>
<html lang="en">
<head>
<meta charset="utf-8">
<title>Elmbrook Memorial – 2024 Gravesite Landscaping Packages</title>
<link href="https://fonts.googleapis.com/css2?family=Poppins:ital,wght@0,400;0,500;0,600;0,700;0,800;1,400&display=swap" rel="stylesheet">
<style>
  :root{
    --maroon:#7b1b2a;
    --maroon-deep:#5a0f19;
    --maroon-dark:#3f0a12;
    --ink:#2b2b2b;
    --card-grey:#ececec;
    --row-grey:#e2e2e2;
    --card-pink:#f3d6db;
    --row-pink:#ebc3ca;
    --tick:#2eb35a;
    --cross:#e0424d;
    --gold:#e2b43a;
    --page:#e9e9e9;
    --white:#ffffff;
  }
  *{box-sizing:border-box;margin:0;padding:0}
  html,body{width:1200px;height:2400px;overflow:hidden;background:var(--page)}
  body{position:relative;font-family:"Poppins",sans-serif;color:var(--ink)}

  .flier{position:absolute;left:0;top:425px;width:838px;height:1082px;background:var(--white);
    transform:scale(1.432);transform-origin:0 0;overflow:hidden}

  .hero-photo{position:absolute;left:0;top:0;width:838px;height:367px;
    background:
      linear-gradient(90deg,rgba(90,15,25,.95) 0%,rgba(110,20,30,.85) 40%,rgba(140,40,30,.3) 70%,rgba(0,0,0,0) 100%),
      linear-gradient(180deg,#d88a2c 0%,#c2541f 45%,#8a2a1c 75%,#6e8a3a 100%)}
  .hero-curve{position:absolute;left:0;top:0;width:838px;height:367px}

  .brand{position:absolute;left:42px;top:58px;display:flex;align-items:center;gap:12px}
  .brand-mark{width:22px;height:22px;border-radius:50%;background:var(--maroon)}
  .brand-name{font-weight:600;font-size:26px;color:var(--maroon);letter-spacing:.5px}

  .title{position:absolute;left:48px;top:152px;color:var(--white);font-weight:800;font-size:51px;line-height:1;letter-spacing:.5px}
  .title-sub{position:absolute;left:50px;top:264px;width:230px;height:30px;background:var(--white);
    color:var(--maroon-dark);font-weight:700;font-size:24px;letter-spacing:8px;text-align:center;line-height:30px;border-radius:3px}

  .badge{position:absolute;left:722px;top:289px;width:62px;height:62px;border-radius:50%;
    background:radial-gradient(circle,#f6d56a 0%,var(--gold) 70%,#b88a1e 100%);
    color:#4a2a00;font-weight:700;font-size:10px;line-height:1.05;text-align:center;
    display:flex;align-items:center;justify-content:center;transform:rotate(-14deg);z-index:3}

  .plans{position:absolute;left:58px;top:317px;width:710px;height:545px}
  .plans-head{position:absolute;left:0;top:0;width:710px;height:117px;background:var(--maroon-deep);
    border-top:3px solid var(--white);border-left:3px solid var(--white);border-top-left-radius:16px;display:flex}
  .plan-head{flex:1;color:var(--white);text-align:center;padding-top:20px;border-right:1px solid rgba(255,255,255,.25)}
  .plan-head:last-child{border-right:none}
  .plan-name{font-weight:700;font-size:19px;line-height:1.05;padding-bottom:6px;margin:0 40px 6px;border-bottom:1px solid rgba(255,255,255,.7)}
  .plan-desc{font-size:12px;line-height:1.25}

  .plans-body{position:absolute;left:0;top:117px;width:710px;height:428px;display:flex;gap:20px;padding:0 13px;
    background:linear-gradient(90deg,#f7f7f7,#fafafa)}
  .plan-card{flex:1;background:var(--card-grey);border-radius:0 0 12px 12px;display:flex;flex-direction:column;overflow:hidden}
  .plan-card.featured{background:var(--card-pink)}
  .row{display:flex;align-items:center;gap:7px;padding:0 14px;font-size:12px;line-height:1.3;height:33px}
  .row.shade{background:var(--row-grey)}
  .featured .row.shade{background:var(--row-pink)}
  .row.tall{height:50px;align-items:flex-start;padding-top:10px}
  .row.tall .icon{margin-top:2px}
  .row.lead{height:44px}
  .icon{flex:none;width:11px;height:11px}
  .weeding{height:108px;text-align:center;padding-top:8px;font-size:12px;line-height:1.25}
  .weeding .icon{display:block;margin:0 auto 4px}
  .weeding-title{color:var(--maroon);font-weight:700;font-size:11.5px}

  .price{flex:1;text-align:center;padding-top:8px}
  .price.shade{background:var(--row-grey)}
  .featured .price.shade{background:var(--row-pink)}
  .price-line{display:flex;align-items:center;justify-content:center;gap:8px}
  .price-label{font-size:11.5px;line-height:1.1;text-align:left;font-weight:500}
  .price-amount{font-weight:700;font-size:27px;color:var(--maroon);line-height:1}
  .price-note{font-size:7.5px;line-height:1.5;margin-top:4px}
  .price-note em{font-style:italic}
  .terms{display:flex;justify-content:center;gap:6px}
  .term{width:52px;background:var(--white);border-radius:3px;overflow:hidden;font-size:10px;font-weight:600;line-height:15px}
  .term b{display:block;background:var(--maroon);color:var(--white);font-size:10px}

  .proof{position:absolute;top:890px;width:176px;height:154px}
  .proof-before{left:56px}
  .proof-after{left:243px}
  .proof-photo{width:176px;height:117px;border-radius:4px;background:linear-gradient(180deg,#8f9486 0%,#6f9a3e 30%,#5c9a2e 100%)}
  .proof-label{margin-top:5px;height:32px;border-radius:0 0 10px 10px;color:var(--white);font-weight:600;font-size:19px;text-align:center;line-height:32px}
  .proof-before .proof-label{background:#333}
  .proof-after .proof-label{background:var(--maroon)}

  .contact{position:absolute;left:448px;top:893px}
  .contact-title{font-weight:700;font-size:19px;letter-spacing:5px;color:var(--maroon)}
  .contact-line{display:flex;align-items:center;gap:10px;font-size:20px;font-weight:500;margin-top:8px;line-height:26px}
  .contact-line svg{width:18px;height:18px;fill:var(--maroon)}
  .web{position:absolute;left:455px;top:1005px;width:383px;height:35px;background:var(--maroon);
    color:var(--white);font-weight:600;font-size:20px;line-height:35px;padding-left:16px;box-shadow:0 3px 4px rgba(0,0,0,.3)}
</style>
</head>
<body>
<main class="flier">
  <div class="hero-photo" role="img" aria-label="Autumn trees with orange and red foliage over a cemetery lawn"></div>
  <svg class="hero-curve" viewBox="0 0 838 367" aria-hidden="true">
    <path d="M0 0 H528 C480 70 440 128 300 132 H0 Z" fill="#fff"/>
    <rect x="0" y="367" width="838" height="0" fill="#fff"/>
  </svg>

  <header class="brand">
    <span class="brand-mark"></span>
    <span class="brand-name">Elmbrook Memorial</span>
  </header>

  <h1 class="title">2024 GRAVESITE<br>LANDSCAPING</h1>
  <div class="title-sub">PACKAGES</div>

  <div class="badge">MOST<br>POPULAR</div>

  <section class="plans">
    <div class="plans-head">
      <div class="plan-head"><div class="plan-name">Seasonal<br>Care</div><div class="plan-desc">Seasonal landscaping<br>grave care</div></div>
      <div class="plan-head"><div class="plan-name">Basic Care<br>Endowment</div><div class="plan-desc">Landscaping care forever for<br>graves with no plantings.</div></div>
      <div class="plan-head"><div class="plan-name">Perpetual Care<br>Endowment</div><div class="plan-desc">Landscaping care forever for<br>graves with plantings.</div></div>
    </div>

    <div class="plans-body">
      <article class="plan-card">
        <div class="weeding"><svg class="icon" viewBox="0 0 12 12"><circle cx="6" cy="6" r="6" fill="#2eb35a"/><path d="M3.2 6.2l1.8 1.8 3.8-4" stroke="#fff" stroke-width="1.6" fill="none"/></svg>
          <div class="weeding-title">WEEDING &amp; TRIMMING</div>Approximately every 7 weeks<br>during the growing season :<br>mid-April through<br>mid-October</div>
        <div class="row lead shade"><svg class="icon" viewBox="0 0 12 12"><circle cx="6" cy="6" r="6" fill="#e0424d"/><path d="M4 4l4 4M8 4l-4 4" stroke="#fff" stroke-width="1.5"/></svg>Monument Leveling</div>
        <div class="row tall"><svg class="icon" viewBox="0 0 12 12"><circle cx="6" cy="6" r="6" fill="#e0424d"/><path d="M4 4l4 4M8 4l-4 4" stroke="#fff" stroke-width="1.5"/></svg>Payment ensures grave<br>care forever</div>
        <div class="row shade"><svg class="icon" viewBox="0 0 12 12"><circle cx="6" cy="6" r="6" fill="#e0424d"/><path d="M4 4l4 4M8 4l-4 4" stroke="#fff" stroke-width="1.5"/></svg>Monument Cleaning</div>
        <div class="row"><svg class="icon" viewBox="0 0 12 12"><circle cx="6" cy="6" r="6" fill="#e0424d"/><path d="M4 4l4 4M8 4l-4 4" stroke="#fff" stroke-width="1.5"/></svg>Full bed of Boxwood Shrubs</div>
        <div class="row shade"><svg class="icon" viewBox="0 0 12 12"><circle cx="6" cy="6" r="6" fill="#e0424d"/><path d="M4 4l4 4M8 4l-4 4" stroke="#fff" stroke-width="1.5"/></svg>Replacement of Shrubs</div>
        <div class="row"><svg class="icon" viewBox="0 0 12 12"><circle cx="6" cy="6" r="6" fill="#e0424d"/><path d="M4 4l4 4M8 4l-4 4" stroke="#fff" stroke-width="1.5"/></svg>Trust Certificate</div>
        <div class="price shade">
          <div class="terms">
            <div class="term">3 years<b>$462</b></div>
            <div class="term">2 years<b>$308</b></div>
            <div class="term">1 year<b>$154</b></div>
          </div>
          <p class="price-note">Multi-year payment locks in current rates<br><em>Valid through 10/31/2024</em></p>
        </div>
      </article>

      <article class="plan-card">
        <div class="weeding"><svg class="icon" viewBox="0 0 12 12"><circle cx="6" cy="6" r="6" fill="#2eb35a"/><path d="M3.2 6.2l1.8 1.8 3.8-4" stroke="#fff" stroke-width="1.6" fill="none"/></svg>
          <div class="weeding-title">WEEDING &amp; TRIMMING</div>2 times per year :<br>mid-May &amp;<br>mid-September</div>
        <div class="row lead shade"><svg class="icon" viewBox="0 0 12 12"><circle cx="6" cy="6" r="6" fill="#2eb35a"/><path d="M3.2 6.2l1.8 1.8 3.8-4" stroke="#fff" stroke-width="1.6" fill="none"/></svg>Monument Leveling</div>
        <div class="row tall"><svg class="icon" viewBox="0 0 12 12"><circle cx="6" cy="6" r="6" fill="#2eb35a"/><path d="M3.2 6.2l1.8 1.8 3.8-4" stroke="#fff" stroke-width="1.6" fill="none"/></svg>Payment ensures grave<br>care forever</div>
        <div class="row shade"><svg class="icon" viewBox="0 0 12 12"><circle cx="6" cy="6" r="6" fill="#e0424d"/><path d="M4 4l4 4M8 4l-4 4" stroke="#fff" stroke-width="1.5"/></svg>Monument Cleaning</div>
        <div class="row"><svg class="icon" viewBox="0 0 12 12"><circle cx="6" cy="6" r="6" fill="#e0424d"/><path d="M4 4l4 4M8 4l-4 4" stroke="#fff" stroke-width="1.5"/></svg>Full bed of Boxwood Shrubs</div>
        <div class="row shade"><svg class="icon" viewBox="0 0 12 12"><circle cx="6" cy="6" r="6" fill="#e0424d"/><path d="M4 4l4 4M8 4l-4 4" stroke="#fff" stroke-width="1.5"/></svg>Replacement of Shrubs</div>
        <div class="row"><svg class="icon" viewBox="0 0 12 12"><circle cx="6" cy="6" r="6" fill="#e0424d"/><path d="M4 4l4 4M8 4l-4 4" stroke="#fff" stroke-width="1.5"/></svg>Trust Certificate</div>
        <div class="price shade">
          <div class="price-line"><span class="price-label">12 monthly<br>payments of</span><span class="price-amount">$328</span></div>
          <p class="price-note">Call for single payment discount.<br><em>Valid through 10/31/2024</em></p>
        </div>
      </article>

      <article class="plan-card featured">
        <div class="weeding"><svg class="icon" viewBox="0 0 12 12"><circle cx="6" cy="6" r="6" fill="#2eb35a"/><path d="M3.2 6.2l1.8 1.8 3.8-4" stroke="#fff" stroke-width="1.6" fill="none"/></svg>
          <div class="weeding-title">WEEDING &amp; TRIMMING</div>Approximately every 7 weeks<br>during the growing season :<br>mid-April through<br>mid-October</div>
        <div class="row lead shade"><svg class="icon" viewBox="0 0 12 12"><circle cx="6" cy="6" r="6" fill="#2eb35a"/><path d="M3.2 6.2l1.8 1.8 3.8-4" stroke="#fff" stroke-width="1.6" fill="none"/></svg>Monument Leveling</div>
        <div class="row tall"><svg class="icon" viewBox="0 0 12 12"><circle cx="6" cy="6" r="6" fill="#2eb35a"/><path d="M3.2 6.2l1.8 1.8 3.8-4" stroke="#fff" stroke-width="1.6" fill="none"/></svg>Payment ensures grave<br>care forever</div>
        <div class="row shade"><svg class="icon" viewBox="0 0 12 12"><circle cx="6" cy="6" r="6" fill="#2eb35a"/><path d="M3.2 6.2l1.8 1.8 3.8-4" stroke="#fff" stroke-width="1.6" fill="none"/></svg>Monument Cleaning</div>
        <div class="row"><svg class="icon" viewBox="0 0 12 12"><circle cx="6" cy="6" r="6" fill="#2eb35a"/><path d="M3.2 6.2l1.8 1.8 3.8-4" stroke="#fff" stroke-width="1.6" fill="none"/></svg>Full bed of Boxwood Shrubs</div>
        <div class="row shade"><svg class="icon" viewBox="0 0 12 12"><circle cx="6" cy="6" r="6" fill="#2eb35a"/><path d="M3.2 6.2l1.8 1.8 3.8-4" stroke="#fff" stroke-width="1.6" fill="none"/></svg>Replacement of Shrubs</div>
        <div class="row"><svg class="icon" viewBox="0 0 12 12"><circle cx="6" cy="6" r="6" fill="#2eb35a"/><path d="M3.2 6.2l1.8 1.8 3.8-4" stroke="#fff" stroke-width="1.6" fill="none"/></svg>Trust Certificate</div>
        <div class="price shade">
          <div class="price-line"><span class="price-label">12 monthly<br>payments of</span><span class="price-amount">$404</span></div>
          <p class="price-note">Call for single payment discount.<br><em>Valid through 10/31/2024</em></p>
        </div>
      </article>
    </div>
  </section>

  <figure class="proof proof-before">
    <div class="proof-photo" role="img" aria-label="Overgrown gravesite with untrimmed shrubs before care"></div>
    <figcaption class="proof-label">Before Care</figcaption>
  </figure>
  <figure class="proof proof-after">
    <div class="proof-photo" role="img" aria-label="Neatly trimmed gravesite with tidy boxwood after care"></div>
    <figcaption class="proof-label">After Care</figcaption>
  </figure>

  <section class="contact">
    <h2 class="contact-title">CONTACT US</h2>
    <p class="contact-line"><svg viewBox="0 0 24 24"><path d="M6.6 10.8a15.1 15.1 0 0 0 6.6 6.6l2.2-2.2a1 1 0 0 1 1-.25 11.4 11.4 0 0 0 3.6.57 1 1 0 0 1 1 1V20a1 1 0 0 1-1 1A17 17 0 0 1 3 4a1 1 0 0 1 1-1h3.5a1 1 0 0 1 1 1c0 1.25.2 2.45.57 3.57a1 1 0 0 1-.25 1z"/></svg>(201) 555-0143</p>
    <p class="contact-line"><svg viewBox="0 0 24 24"><path d="M2 5h20v14H2z M3 6l9 7 9-7" fill="none" stroke="#7b1b2a" stroke-width="2"/></svg>info@elmbrookmemorial.org</p>
  </section>
  <div class="web">www.elmbrookmemorial.org</div>
</main>
</body>
</html>
```